Classy, Elegant, Simple Business Card Design

Looking to have a classy, simple, and elegant design. Want a top notch designed business card. I really like the look of the new brivo credit card. I also like the design I attached. I am trying to reach 21-29 year old females for booking us for there wedding or event. We offer Disc Jockey Service, Photo Booth Rentals, and Uplighting .

Target Market(s)

21-28 year old females

Contact Information for Business Card

Has to have logo, website, email, and phone number

Font styles to use
Other font styles liked:
• open to font choice, modern, clean
Designer to choose
33a6d7
0791cd
0555a3
ffffff

Requirements
Must have
• Has to have logo, website, email, and phone number
Nice to have
• I really like the design of the new brivo credit card. I also included my logo and some designs I like
Should not have
• clutter or too much info

```html
<!DOCTYPE html>
<html lang="en">
<head>
<meta charset="utf-8">
<title>Echolane Event Group – Business Card</title>
<link rel="stylesheet" href="https://fonts.googleapis.com/css2?family=Jost:wght@400;500&display=swap">
<style>
  :root {
    --page-bg: #f5f5f5;
    --card-bg: #262626;
    --text-light: #ffffff;
    --brand-grey: #d4d4d4;
  }
  * { margin: 0; padding: 0; box-sizing: border-box; }
  html, body {
    width: 1200px;
    height: 900px;
    overflow: hidden;
    background: var(--page-bg);
    font-family: "Jost", sans-serif;
  }
  .canvas {
    position: relative;
    width: 1200px;
    height: 900px;
  }
  .card {
    position: absolute;
    left: 288px;
    width: 624px;
    height: 356px;
    background: var(--card-bg);
  }
  .card--front { top: 80px; }
  .card--back { top: 465px; }

  .front-brand {
    position: absolute;
    left: 0;
    right: 0;
    top: 145px;
    text-align: center;
    font-size: 52px;
    font-weight: 500;
    color: var(--brand-grey);
    line-height: 1;
  }

  .back-brand {
    position: absolute;
    left: 30px;
    width: 270px;
    top: 158px;
    text-align: center;
    font-size: 18px;
    font-weight: 500;
    letter-spacing: 1px;
    text-transform: uppercase;
    color: var(--brand-grey);
    line-height: 1;
  }

  .divider {
    position: absolute;
    left: 303px;
    top: 125px;
    width: 2px;
    height: 102px;
    background: var(--text-light);
  }

  .contact {
    position: absolute;
    left: 327px;
    top: 118px;
    color: var(--text-light);
  }
  .contact__name {
    font-size: 21px;
    font-weight: 500;
    letter-spacing: 0.5px;
    line-height: 30px;
    margin-bottom: 10px;
  }
  .contact__line {
    font-size: 16px;
    font-weight: 400;
    line-height: 25px;
    letter-spacing: 0.2px;
  }
</style>
</head>
<body>
  <main class="canvas">
    <section class="card card--front" aria-label="Card front">
      <p class="front-brand">Echolane</p>
    </section>

    <section class="card card--back" aria-label="Card back">
      <p class="back-brand">Echolane Event Group</p>
      <div class="divider"></div>
      <div class="contact">
        <p class="contact__name">Daniel K. Mercer</p>
        <p class="contact__line">555 014 2963</p>
        <p class="contact__line">info@echolaneeventgroup.com</p>
        <p class="contact__line">www.echolaneeventgroup.com</p>
      </div>
    </section>
  </main>
</body>
</html>
```